Flyer for Compassion training days

I need a A5-size, single-sided flyer design for my training days. They are weekends in a blend of Compassionate Communication and Buddhist teachings called Palomere Communication. The logo for Palomere that should be included.
The flyer needs room for 1) course title, 2) course dates, location & price, 3) course description, 4) booking info, 5) my picture & short bio, and 6) the palomere.co website (yes, it is 'co' and not 'com).
Updates

Target Market(s)

Women 35-65 years, well-educated, spiritually minded. May have interests like yoga and meditation.

Industry/Entity Type

Health And Wellness

Font styles to use
Sans Serif
Other font styles liked:
• Blue Plaque, Josefina are both great

Colors
fbf289
fdf9cf
cfeae6
33b8a4

Requirements
Must have
• The Palomere logo; my picture.
• Elegance. Calm and expansive feel.
• The poster provided in the project files shows you the kind of information I need to include.
• Colours -- greens and yellows, but the options on pixel harbor are not quite the right shades.
• The logo colour can be changed.
Nice to have
• Classy (but not cliche) image associated with Buddhism; gentle curves similar to those on the business card (see project files).
Should not have
• Dark background. Busy, loud design. Overly 'swirly' design. Images that I have to buy separately.

```html
<!DOCTYPE html>
<html lang="en">
<head>
<meta charset="utf-8">
<title>Palomere Communication – Core Course</title>
<link rel="stylesheet" href="https://fonts.googleapis.com/css2?family=Lato:wght@400;700&family=Playfair+Display:wght@700;800&display=swap">
<style>
  :root {
    --cream: #f8f4d6;
    --blush: #f7d9e5;
    --white-glow: #fffdf8;
    --green: #8fca5c;
    --green-deep: #5fb163;
    --green-text: #6cb650;
    --brown: #7b5a49;
    --tan: #b58d72;
    --body: #6a4a52;
    --petal: #f19bb5;
    --petal-soft: #f8c7d6;
    --sepia-light: #c9a77e;
    --sepia-dark: #5a3f25;
  }
  * { box-sizing: border-box; margin: 0; padding: 0; }
  html, body { width: 969px; height: 1200px; overflow: hidden; background: #ececec; }
  .flyer {
    position: relative; width: 969px; height: 1200px; overflow: hidden;
    background:
      radial-gradient(ellipse 420px 380px at 720px 700px, var(--white-glow) 0%, rgba(255,253,248,0) 70%),
      radial-gradient(ellipse 300px 260px at 200px 440px, rgba(255,255,255,.7) 0%, rgba(255,255,255,0) 70%),
      linear-gradient(180deg, var(--cream) 0%, #f9ecd8 30%, var(--blush) 60%, #f6d2e0 100%);
    font-family: "Lato", sans-serif;
  }
  .bloom { position: absolute; }
  .bloom--top {
    right: 0; top: 0; width: 290px; height: 360px;
    background: radial-gradient(ellipse 240px 260px at 260px 120px, var(--petal) 0%, var(--petal-soft) 45%, rgba(248,199,214,0) 75%);
  }
  .bloom--bottom {
    left: 0; top: 860px; width: 200px; height: 260px;
    background: radial-gradient(ellipse 170px 190px at 40px 150px, var(--petal) 0%, var(--petal-soft) 50%, rgba(248,199,214,0) 78%);
  }
  .brand {
    position: absolute; left: 40px; top: 70px;
    display: flex; align-items: center; gap: 12px;
    font-family: "Lato", sans-serif; font-weight: 700; font-size: 34px; color: var(--green-deep);
  }
  .brand-dot { width: 22px; height: 22px; border-radius: 50%; background: var(--green-deep); }
  .tagline {
    position: absolute; left: 0; width: 969px; top: 160px; padding-left: 40px;
    text-align: center; font-family: "Playfair Display", serif; font-weight: 700;
    font-size: 27px; line-height: 31px; color: var(--tan);
  }
  .title {
    position: absolute; left: 0; width: 969px; top: 212px; text-align: center;
    font-family: "Playfair Display", serif; font-weight: 800; color: var(--brown);
    font-size: 78px; line-height: 72px; letter-spacing: -1px;
  }
  .course-label {
    position: absolute; left: 0; width: 969px; top: 360px; text-align: center;
    font-size: 40px; color: var(--green-text); letter-spacing: .5px;
  }
  .bands { position: absolute; left: 0; top: 0; }
  .event { position: absolute; left: 0; width: 969px; top: 425px; text-align: center; }
  .event-date { font-family: "Playfair Display", serif; font-weight: 800; font-size: 46px; line-height: 52px; color: #fff; }
  .event-date small { font-size: 36px; }
  .event-venue { font-size: 29px; line-height: 32px; color: var(--brown); }
  .event-price { font-size: 18px; line-height: 24px; color: var(--brown); }
  .column { position: absolute; color: var(--body); font-size: 19.5px; line-height: 20.5px; }
  .column p { margin-bottom: 20px; }
  .column--about { left: 79px; top: 563px; width: 385px; }
  .topics { list-style: none; margin-bottom: 10px; }
  .topics li { position: relative; padding-left: 29px; margin-bottom: 16px; }
  .topics li::before {
    content: ""; position: absolute; left: 2px; top: 6px; width: 10px; height: 10px;
    border-radius: 50%; background: var(--green-deep);
  }
  .column--booking { left: 507px; top: 563px; width: 400px; }
  .portrait {
    position: absolute; left: 510px; top: 617px; width: 358px; height: 322px; border-radius: 50%;
    background: radial-gradient(ellipse at 50% 45%, var(--sepia-light) 0%, #9d7a54 55%, var(--sepia-dark) 100%);
  }
  .column--bio { left: 507px; top: 957px; width: 400px; }
  .site {
    position: absolute; left: 0; width: 969px; top: 1156px; text-align: center;
    font-weight: 700; font-size: 23px; color: #fff; letter-spacing: .5px;
  }
</style>
</head>
<body>
<main class="flyer">
  <div class="bloom bloom--top" role="img" aria-label="Soft pink lotus flower petals"></div>
  <div class="bloom bloom--bottom" role="img" aria-label="Soft pink lotus flower petals"></div>

  <div class="brand"><span class="brand-dot"></span>Palomere</div>

  <p class="tagline">Mindfulness + Kindness +<br>Compassionate Communication =</p>
  <h1 class="title">Palomere<br>Communication</h1>
  <p class="course-label">CORE COURSE</p>

  <svg class="bands" width="969" height="1200" viewBox="0 0 969 1200" aria-hidden="true">
    <path d="M0 402 C280 392 600 412 969 390 L969 522 C720 546 420 548 0 530 Z" fill="var(--green)"/>
    <path d="M0 522 C380 540 700 545 969 515 L969 530 C700 560 380 556 0 540 Z" fill="var(--green-deep)"/>
    <path d="M0 1118 C320 1150 650 1150 969 1112 L969 1200 L0 1200 Z" fill="var(--green)"/>
    <path d="M0 1110 C320 1140 650 1140 969 1102 L969 1112 C650 1150 320 1150 0 1118 Z" fill="var(--green-deep)"/>
  </svg>

  <section class="event">
    <p class="event-date">11–12 <small>Dec</small></p>
    <p class="event-venue">Larkmoor Centre, Edinburgh</p>
    <p class="event-price">(£125/100)</p>
  </section>

  <section class="column column--about">
    <p>Palomere Communication can help you increase awareness &amp; compassion in everyday speech (with yourself &amp; others), better understand your own patterns, and build resilience to challenging situations. Choose from:</p>
    <p>In this 2-day Core Course, we’ll explore:</p>
    <ul class="topics">
      <li>Compassionate Communication;</li>
      <li>Buddhist teachings on Right Speech, loving-kindness, Right Effort, and more;</li>
      <li>mindfulness practices;</li>
      <li>choices available to us in our everyday speech.</li>
    </ul>
    <p>This workshop will be of interest if you’d like to improve personal and/or professional relationships. Open to all, best suited to those with at least 1 year’s experience with Mindfulness, Buddhism, or Compassionate Communication / NVC.</p>
  </section>

  <section class="column column--booking">
    <p>Booking: Book online at TicketGlade or write maribeth@palomere.co</p>
  </section>

  <div class="portrait" role="img" aria-label="Portrait photo of the facilitator, Maribeth Oakhollow"></div>

  <section class="column column--bio">
    <p>Facilitator: Maribeth Oakhollow is an experienced group facilitator, having worked with a range of organisations and presented at a number of festivals &amp; conferences.</p>
    <p>Maribeth offers coaching in Palomere Communication.</p>
  </section>

  <p class="site">WWW.PALOMERE.CO</p>
</main>
</body>
</html>
```